Tulven Electrics Flyer Design Advertising

I am after an A5 Flyer design to help promote my electrical services business.
I would like to have information on what my business offers, photos of electrical work, and specials/deals for an amount of time.

Industry/Entity Type

Electrician

Font styles to use
Sans Serif

Colors
0292cd
33a6d7
85cae6
3176b5
333333
1b1b1b
ffffff
5c5c5c
474747

Requirements
Must have
• Specialising in New homes, renovations and commercial projects
• Contact details:
• ph. 0437 619 458
• email admin@tulvenelectrics.example.au
• facebook TulvenElectrics
• Specials/Deals:
• 10% off all electrical services
• or
• Free LED downlights on installation
• *Terms conditions apply
• ALL RESIDENTIAL & COMMERCIAL ELECTRICAL SERVICES
• - New Home installations
• - Commercial projects
• - Shop fit outs
• - Renovations
• - Smoke Detectors
• - Air Conditioning and Ceiling Fans
• - Garden Lighting
• - Oven and Cooktop Installations
• - Power Point installation
• - LED lighting upgrades
• - Security Lighting
• - Switchboard upgrades
• - Test and Tag
• - Commercial Property
• - General Electrical Maintenance

```html
<!DOCTYPE html>
<html lang="en">
<head>
<meta charset="utf-8">
<title>Tulven Electrics – A5 Flyer</title>
<link href="https://fonts.googleapis.com/css2?family=Roboto:wght@400;500;700&family=Roboto+Condensed:wght@700&display=swap" rel="stylesheet">
<style>
  :root {
    --blue: #0292cd;
    --blue-mid: #33a6d7;
    --blue-light: #85cae6;
    --blue-deep: #3176b5;
    --ink: #333333;
    --ink-dark: #1b1b1b;
    --white: #ffffff;
    --grey: #5c5c5c;
    --grey-dark: #474747;
    --stage: #c9c9c9;
  }
  * { box-sizing: border-box; margin: 0; padding: 0; }
  html, body { width: 1200px; height: 1200px; overflow: hidden; }
  body {
    background: radial-gradient(ellipse at center, #d6d6d6 0%, var(--stage) 70%, #b9b9b9 100%);
    font-family: "Roboto", Arial, sans-serif;
    position: relative;
  }
  .flyer {
    position: absolute;
    top: 232px;
    width: 520px;
    height: 736px;
    background: var(--white);
    overflow: hidden;
    box-shadow: 0 18px 30px rgba(0,0,0,0.25);
  }
  .flyer--front { left: 60px; }
  .flyer--back { left: 620px; }

  .hero {
    position: absolute; left: 0; top: 0; width: 520px; height: 388px;
  }
  .hero__photo { position: absolute; inset: 0; }
  .hero__photo--house {
    background: linear-gradient(180deg, #5b9ad8 0%, #8fbde6 22%, #c9d6d6 42%, #6f8a5e 62%, #3f5a3a 80%, #2e3a36 100%);
  }
  .hero__photo--garden {
    background: linear-gradient(180deg, #4e8fd4 0%, #9cc4e6 20%, #d8e3e4 34%, #5f8a4c 54%, #3d6a3a 72%, #2f4f4a 88%, #2a3d44 100%);
  }
  .hero__shade {
    position: absolute; left: 0; right: 0; bottom: 0; height: 120px;
    background: linear-gradient(180deg, rgba(30,35,40,0) 0%, rgba(30,35,40,0.75) 100%);
  }
  .brand {
    position: absolute; top: 32px; left: 0; right: 0;
    display: flex; align-items: center; justify-content: center; gap: 10px;
  }
  .brand__dot {
    width: 44px; height: 44px; border-radius: 50%;
    background: var(--blue-deep);
  }
  .brand__name {
    font-family: "Roboto", Arial, sans-serif;
    font-weight: 700; font-size: 26px; letter-spacing: 1px;
    color: var(--white); text-transform: uppercase;
  }
  .hero__title {
    position: absolute; left: 0; right: 0;
    text-align: center; color: var(--white);
    font-weight: 500; font-size: 25px; line-height: 1.08;
  }
  .flyer--front .hero__title { top: 318px; }
  .flyer--back .hero__title { top: 320px; font-size: 25px; }
  .hero__subtitle {
    position: absolute; left: 0; right: 0; top: 352px;
    text-align: center; color: var(--white);
    font-size: 12px; font-weight: 500;
  }

  /* front: gallery */
  .gallery-band {
    position: absolute; left: 0; top: 396px; width: 520px; height: 88px;
    background: var(--blue);
  }
  .gallery {
    position: absolute; top: 412px; left: 18px; width: 488px; height: 100px;
  }
  .gallery__shot {
    position: absolute; top: 0; width: 156px; height: 100px;
    border: 3px solid var(--white);
    clip-path: polygon(4% 0, 100% 0, 96% 100%, 0 100%);
  }
  .gallery__shot:nth-child(1) { left: 0; background: linear-gradient(160deg, #1f2f4a 0%, #6a6f7e 45%, #2a9cc2 80%, #7fd0e8 100%); }
  .gallery__shot:nth-child(2) { left: 164px; background: linear-gradient(180deg, #1b1d22 0%, #3d2f25 45%, #b08a5c 70%, #4a3424 100%); }
  .gallery__shot:nth-child(3) { left: 328px; background: linear-gradient(170deg, #d9dfe2 0%, #6f9a5a 35%, #2f5a34 60%, #2a8cb8 100%); }

  .section-title {
    position: absolute; top: 536px; left: 16px; right: 16px;
    display: flex; align-items: center; gap: 10px;
    color: var(--blue-mid); font-size: 24px; font-weight: 500;
  }
  .section-title::before, .section-title::after {
    content: ""; flex: 1; height: 2px; background: var(--blue-mid);
  }

  .offers-band {
    position: absolute; left: 0; top: 630px; width: 520px; height: 77px;
    background: var(--blue-light);
  }
  .offer {
    position: absolute; top: 570px; height: 96px;
    display: flex;
  }
  .offer--discount { left: 18px; width: 222px; }
  .offer--led { left: 278px; width: 228px; }
  .offer__badge {
    width: 92px; background: var(--blue-deep); color: var(--white);
    border-radius: 8px 0 0 8px;
    font-family: "Roboto Condensed", Arial, sans-serif; font-weight: 700;
    display: flex; flex-direction: column; justify-content: center; align-items: center;
    font-size: 38px; line-height: 1;
  }
  .offer__detail {
    flex: 1; background: var(--white);
    border: 1.5px dashed var(--blue-deep); border-left: none;
    border-radius: 0 8px 8px 0;
    display: flex; flex-direction: column; justify-content: center; align-items: center;
    color: var(--ink); line-height: 1.05; text-align: center;
  }
  .offer__small { font-size: 13px; }
  .offer__mid { font-size: 18px; }
  .offer__strong {
    font-family: "Roboto Condensed", Arial, sans-serif; font-weight: 700;
    color: var(--blue-deep); font-size: 28px;
  }
  .offer--led .offer__strong { font-size: 21px; }
  .offers-or {
    position: absolute; left: 247px; top: 604px; width: 26px;
    color: var(--blue-deep); font-size: 22px; font-weight: 500;
    transform: rotate(-90deg); text-align: center;
  }

  .contact {
    position: absolute; left: 0; width: 520px; height: 77px;
    display: flex; align-items: center; color: var(--white);
  }
  .flyer--front .contact { top: 668px; height: 40px; }
  .flyer--back .contact { top: 659px; background: var(--blue); }
  .contact__phone {
    width: 260px; display: flex; align-items: center; justify-content: center; gap: 10px;
    font-size: 26px; font-weight: 500;
  }
  .contact__divider { width: 1.5px; height: 42px; background: var(--white); }
  .contact__online {
    padding-left: 22px; font-size: 12.5px; font-weight: 700; line-height: 1.5;
  }
  .contact__line { display: flex; align-items: center; gap: 6px; }
  .contact__square { width: 10px; height: 10px; background: var(--white); border-radius: 1px; }
  .terms {
    position: absolute; top: 712px; left: 0; right: 0; text-align: center;
    font-size: 13px; color: var(--ink-dark);
  }

  /* back: service list */
  .services {
    position: absolute; top: 412px; left: 24px; right: 20px;
    display: flex;
  }
  .services__col { list-style: none; }
  .services__col--a { width: 230px; padding-right: 14px; border-right: 1px solid #dedede; }
  .services__col--b { padding-left: 16px; }
  .services__item {
    position: relative; padding-left: 13px;
    font-size: 14.5px; color: var(--grey); line-height: 19px; margin-bottom: 8.5px;
  }
  .services__item::before {
    content: ""; position: absolute; left: 0; top: 6px;
    width: 7px; height: 7px; border-radius: 50%; background: var(--grey-dark);
  }
</style>
</head>
<body>

<section class="flyer flyer--front" aria-label="Flyer front – specials">
  <div class="hero">
    <div class="hero__photo hero__photo--house" role="img" aria-label="Photo of a new white two-storey home with garage and tropical garden"></div>
    <div class="hero__shade"></div>
    <div class="brand">
      <span class="brand__dot"></span>
      <span class="brand__name">Tulven Electrics</span>
    </div>
    <h1 class="hero__title">SPECIALISING IN NEW HOMES</h1>
    <p class="hero__subtitle">RENOVATIONS AND COMMERCIAL PROJECTS</p>
  </div>

  <div class="gallery-band"></div>
  <div class="gallery">
    <div class="gallery__shot" role="img" aria-label="Photo of a modern home lit at dusk beside a pool"></div>
    <div class="gallery__shot" role="img" aria-label="Photo of an outdoor lounge with warm wall lights at night"></div>
    <div class="gallery__shot" role="img" aria-label="Photo of a garden patio with lighting and pool"></div>
  </div>

  <h2 class="section-title">SPECIALS/DEALS</h2>

  <div class="offers-band"></div>
  <div class="offer offer--discount">
    <div class="offer__badge"><span>10%</span><span>OFF</span></div>
    <div class="offer__detail">
      <span class="offer__small">ALL</span>
      <span class="offer__mid">ELECTRICAL</span>
      <span class="offer__strong">SERVICES</span>
    </div>
  </div>
  <div class="offers-or">OR</div>
  <div class="offer offer--led">
    <div class="offer__badge"><span>FREE</span><span>LED</span></div>
    <div class="offer__detail">
      <span class="offer__mid">DOWNLIGHTS</span>
      <span class="offer__small">ON</span>
      <span class="offer__strong">INSTALLATION</span>
    </div>
  </div>

  <div class="contact">
    <div class="contact__phone">
      <svg width="22" height="24" viewBox="0 0 22 24" aria-hidden="true"><rect x="0" y="0" width="22" height="24" rx="5" fill="#fff"/><path d="M7 5c1 0 2 3 1.5 4s-1 1 0 3 2 3 3 3 1.5-1 2.5-.5 2.5 1.5 2 2.5-2 2-4 1-6-5-6.5-8S6 5 7 5z" fill="#85cae6"/></svg>
      <span>0437 619 458</span>
    </div>
    <div class="contact__divider"></div>
    <div class="contact__online">
      <div class="contact__line"><svg width="11" height="8" viewBox="0 0 11 8" aria-hidden="true"><rect width="11" height="8" fill="#fff"/><path d="M0 0l5.5 4.5L11 0" stroke="#85cae6" fill="none"/></svg>admin@tulvenelectrics.example.au</div>
      <div class="contact__line"><span class="contact__square"></span>TulvenElectrics</div>
    </div>
  </div>
  <p class="terms">*Terms conditions apply</p>
</section>

<section class="flyer flyer--back" aria-label="Flyer back – services">
  <div class="hero">
    <div class="hero__photo hero__photo--garden" role="img" aria-label="Photo of a tropical garden pavilion with pool and outdoor lounge"></div>
    <div class="hero__shade"></div>
    <div class="brand">
      <span class="brand__dot"></span>
      <span class="brand__name">Tulven Electrics</span>
    </div>
    <h1 class="hero__title">ALL RESIDENTIAL &amp; COMMERCIAL<br>ELECTRICAL SERVICES</h1>
  </div>

  <div class="services">
    <ul class="services__col services__col--a">
      <li class="services__item">New Home installations</li>
      <li class="services__item">Commercial projects</li>
      <li class="services__item">Shop fit outs</li>
      <li class="services__item">Renovations</li>
      <li class="services__item">Smoke Detectors</li>
      <li class="services__item">Air Conditioning and Ceiling Fans</li>
      <li class="services__item">Garden Lighting</li>
    </ul>
    <ul class="services__col services__col--b">
      <li class="services__item">Oven and Cooktop Installations</li>
      <li class="services__item">Power Point installation</li>
      <li class="services__item">LED lighting upgrades</li>
      <li class="services__item">Security Lighting</li>
      <li class="services__item">Switchboard upgrades</li>
      <li class="services__item">Test and Tag</li>
      <li class="services__item">Commercial Property</li>
      <li class="services__item">General Electrical Maintenance</li>
    </ul>
  </div>

  <div class="contact">
    <div class="contact__phone">
      <svg width="22" height="24" viewBox="0 0 22 24" aria-hidden="true"><rect x="0" y="0" width="22" height="24" rx="5" fill="#fff"/><path d="M7 5c1 0 2 3 1.5 4s-1 1 0 3 2 3 3 3 1.5-1 2.5-.5 2.5 1.5 2 2.5-2 2-4 1-6-5-6.5-8S6 5 7 5z" fill="#0292cd"/></svg>
      <span>0437 619 458</span>
    </div>
    <div class="contact__divider"></div>
    <div class="contact__online">
      <div class="contact__line"><svg width="11" height="8" viewBox="0 0 11 8" aria-hidden="true"><rect width="11" height="8" fill="#fff"/><path d="M0 0l5.5 4.5L11 0" stroke="#0292cd" fill="none"/></svg>admin@tulvenelectrics.example.au</div>
      <div class="contact__line"><span class="contact__square"></span>TulvenElectrics</div>
    </div>
  </div>
</section>

</body>
</html>
```